VORLANE (PTY)LTD Website design

WEBSITE design based on our different divisions in our organization.
Our company specializes in the following.
Construction
Property development
Demolition
Mining
Transport
Manufacturing of concrete bricks and blocks
Lightweight concrete Readymix
I want a very modern website and look that fits in with our organization and the changing times of the world.
The website must be very professional and crisp and should appeal to both the younger generation and older generation of business leaders and.
The website must be very user friendly and easy to navigate, simple yet modern, professional and corporate.

```html
<!DOCTYPE html>
<html lang="en">
<head>
<meta charset="utf-8">
<title>VORLANE (PTY)LTD</title>
<link rel="stylesheet" href="https://fonts.googleapis.com/css2?family=Roboto:wght@400;500;700&family=Roboto+Condensed:wght@400;700&family=Roboto+Slab:wght@400;700&display=swap">
<style>
:root{
  --blue:#1b86d4;
  --blue-bright:#2592e0;
  --blue-light:#3aa4f0;
  --blue-dark:#0d3f78;
  --navy:#0a2a52;
  --panel:#cfe5f7;
  --ink:#222;
  --white:#fff;
  --field:rgba(255,255,255,.14);
}
*{box-sizing:border-box;margin:0;padding:0}
html,body{width:1200px;height:3448px;overflow:hidden}
body{position:relative;background:var(--white);font-family:"Roboto",Arial,sans-serif;color:var(--ink)}
.abs{position:absolute}
.center{left:0;width:1200px;text-align:center}

/* header */
.topline{left:0;top:0;width:1200px;height:5px;background:var(--blue)}
.corner{right:0;top:0}
.brand{left:133px;top:36px;font-family:"Roboto Condensed",sans-serif;font-weight:700;font-size:56px;color:var(--blue);letter-spacing:2px;line-height:1}
.contact-top{left:712px;top:20px;font-size:15px;color:#444;display:flex;gap:28px;align-items:center}
.contact-top span{display:flex;align-items:center;gap:8px}
.nav{left:508px;top:76px;display:flex;font-family:"Roboto Condensed",sans-serif;font-size:19px}
.nav a{color:#222;text-decoration:none;padding:0 21px}
.nav a.active{color:var(--blue);font-weight:700}

/* hero */
.hero{left:0;top:110px;width:1200px;height:592px;clip-path:polygon(0 0,100% 0,100% 86%,0 100%);
  background:linear-gradient(160deg,#5f9bd0 0%,#3f7fbd 40%,#2a66a6 75%,#6d9cc9 100%)}
.hero-title{top:333px;font-family:"Roboto Condensed",sans-serif;font-size:40px;color:var(--white)}
.hero-sub{top:387px;font-family:"Roboto Condensed",sans-serif;font-size:31px;color:var(--white)}
.arrow{top:354px;width:34px;height:30px;background:#333;display:flex;align-items:center;justify-content:center}
.btn{display:inline-block;font-family:"Roboto Condensed",sans-serif;font-size:13px;text-transform:uppercase;color:var(--blue);
  border:2px solid var(--blue);padding:6px 10px;box-shadow:5px 5px 0 -2px #a9d1f0;background:var(--white)}
.btn-wrap{left:0;width:1200px;text-align:center}

/* headings */
.h2{font-family:"Roboto Condensed",sans-serif;font-size:34px;color:var(--blue)}
.h2 b{color:var(--blue-dark);font-weight:400}
.copy{left:150px;width:900px;text-align:center;font-size:12.5px;line-height:22px;color:#222}
.copy p+p{margin-top:6px}
.rule{width:50px;height:2px;background:var(--blue);left:575px}

/* services */
.services{left:0;top:1020px;width:1200px;height:720px;background:var(--blue-bright);clip-path:polygon(0 0,100% 7%,100% 100%,0 100%)}
.services-photo{left:0;top:0;width:1200px;height:720px;background:linear-gradient(180deg,rgba(255,255,255,.08),rgba(0,0,0,0) 60%)}
.tabs{left:133px;top:1306px;width:260px}
.tab{height:44px;display:flex;align-items:center;gap:14px;padding-left:8px;font-family:"Roboto Slab",serif;font-size:15px;color:var(--white);line-height:17px}
.tab.active{background:var(--blue-dark)}
.tab-ico{width:28px;height:22px;border:2px solid rgba(255,255,255,.9);border-radius:3px;flex:none}
.panel{left:398px;top:1306px;width:671px;height:344px;background:var(--panel);border:2px solid #9ccbee}
.panel h3{position:absolute;left:14px;top:14px;font-family:"Roboto Slab",serif;font-size:15px;color:#111}
.panel p{position:absolute;left:14px;top:44px;width:262px;font-size:12.5px;line-height:22px;color:#222}
.panel .btn{position:absolute;left:20px;top:278px;background:transparent}
.panel-photo{position:absolute;left:290px;top:30px;width:368px;height:240px;border:3px solid #d8b56a;
  background:linear-gradient(150deg,#7bb2e6 0%,#2f6fb5 45%,#c89a4a 80%,#e8d27a 100%)}

/* why choose */
.why{left:0;top:2030px;width:1200px;height:464px;background:linear-gradient(100deg,#0e4789 0%,#1a61ad 45%,#0f4a8f 100%)}
.arc{left:440px;top:2322px;width:320px;height:320px;border-radius:50%;background:var(--white)}
.arc-brand{top:2390px;font-family:"Roboto Condensed",sans-serif;font-weight:700;font-size:46px;color:var(--blue);letter-spacing:2px}
.feat-ico{width:78px;height:78px;border-radius:50%;background:var(--white);border:3px solid #9ccbee;display:flex;align-items:center;justify-content:center}
.feat{color:var(--white);font-size:12.5px;line-height:17px}
.feat h4{font-family:"Roboto Condensed",sans-serif;font-size:16px;font-weight:700;line-height:18px;margin-bottom:4px}
.feat.r{text-align:right}
.dot{width:12px;height:12px;border-radius:50%;background:var(--white);border:2px solid var(--blue)}

/* contact */
.contact{left:0;top:2760px;width:1200px;height:643px;clip-path:polygon(0 0,100% 9%,100% 100%,0 100%);
  background:linear-gradient(180deg,#2b3a4e 0%,#1d2a3b 55%,#38332e 100%)}
.c-line{font-family:"Roboto Slab",serif;font-size:15px;color:var(--white);display:flex;justify-content:center;gap:10px;align-items:center}
.field{background:var(--field);border:1px solid rgba(255,255,255,.2);color:#e6e6e6;font-size:13px;padding:10px 12px}
.send{left:471px;top:3303px;width:258px;height:46px;background:var(--blue);color:var(--white);font-family:"Roboto Condensed",sans-serif;font-weight:700;font-size:22px;display:flex;align-items:center;justify-content:center}
.footer{left:0;top:3403px;width:1200px;height:45px;background:#10243f;border-top:6px solid var(--blue);color:#ddd;font-family:"Roboto Slab",serif;font-size:12px;display:flex;align-items:center;justify-content:center}
</style>
</head>
<body>

<!-- header -->
<div class="abs topline"></div>
<svg class="abs corner" width="130" height="70" viewBox="0 0 130 70"><polygon points="40,0 130,0 130,70" fill="#0d3f78"/><polygon points="10,0 60,0 130,55 130,70" fill="#1b86d4"/></svg>
<div class="abs brand">VORLANE</div>
<div class="abs contact-top">
  <span><svg width="22" height="15" viewBox="0 0 22 15"><rect x="1" y="1" width="20" height="13" fill="none" stroke="#1b86d4" stroke-width="2"/><path d="M1 1l10 8 10-8" fill="none" stroke="#1b86d4" stroke-width="2"/></svg>info@vorlane.co.za</span>
  <span><svg width="16" height="18" viewBox="0 0 16 18"><path d="M3 1l4 4-2 3c1 2 3 4 5 5l3-2 3 4-2 2C8 17 0 9 1 3z" fill="#1b86d4"/></svg>+27 (0) 21 555 0148</span>
</div>
<nav class="abs nav">
  <a class="active">Home</a><a>About Us</a><a>Services</a><a>Why Choose Us</a><a>Contact Us</a>
</nav>

<!-- hero -->
<div class="abs hero" role="img" aria-label="Construction workers laying concrete blocks on a building site, tinted blue"></div>
<div class="abs arrow" style="left:4px"><svg width="10" height="14"><path d="M9 1L2 7l7 6" fill="#fff"/></svg></div>
<div class="abs arrow" style="right:4px"><svg width="10" height="14"><path d="M1 1l7 6-7 6" fill="#fff"/></svg></div>
<div class="abs center hero-title">We Provide World Class Quality Design &amp; Construction</div>
<div class="abs center hero-sub">Are you interested in an estimate ?</div>
<div class="abs btn-wrap" style="top:436px"><span class="btn">Contact Us Today</span></div>

<!-- about -->
<div class="abs center h2" style="top:735px">ABOUT VORLANE <b>BUILDING FORWARD</b></div>
<div class="abs rule" style="top:785px"></div>
<div class="abs copy" style="top:796px">
  <p>Lorem ipsum dolor sit amet, consectetuer adipiscing elit, sed diam nonummy nibh euismod tincidunt ut laoreet dolore magna aliquam erat volutpat. Ut wisi enim ad minim veniam, quis nostrud exerci tation ullamcorper suscipit lobortis nisl ut aliquip ex ea commodo consequat. Duis autem vel eum iriure dolor in hendrerit in vulputate velit esse molestie consequat, vel illum dolore eu feugiat nulla facilisis at vero eros et accumsan et iusto odio dignissim qui blandit praesent luptatum zzril delenit augue duis dolore te feugait nulla facilisi.</p>
  <p>Lorem ipsum dolor sit amet, consectetuer adipiscing elit, sed diam nonummy nibh euismod tincidunt ut laoreet dolore magna aliquam erat volutpat. Ut wisi enim ad minim veniam, quis nostrud exerci tation ullamcorper suscipit lobortis nisl ut aliquip ex ea commodo consequat.</p>
</div>
<div class="abs btn-wrap" style="top:960px"><span class="btn">Read More</span></div>

<!-- services -->
<div class="abs services" role="img" aria-label="Blue tinted view of tower cranes over a construction site"><div class="abs services-photo"></div></div>
<div class="abs center h2" style="top:1148px;color:#fff">OUR SERVICES</div>
<div class="abs rule" style="top:1198px;background:#fff"></div>
<div class="abs copy" style="top:1228px;color:#fff">Lorem ipsum dolor sit amet, consectetuer adipiscing elit, sed diam nonummy nibh euismod tincidunt ut laoreet dolore magna aliquam erat volutpat. Ut wisi enim ad minim veniam, quis nostrud exerci tation ullamcorper suscipit lobortis nisl ut aliquip ex ea commodo consequat.</div>
<div class="abs tabs">
  <div class="tab active"><span class="tab-ico"></span>Construction</div>
  <div class="tab"><span class="tab-ico"></span>Property Development</div>
  <div class="tab"><span class="tab-ico"></span>Demolition</div>
  <div class="tab"><span class="tab-ico"></span>Mining</div>
  <div class="tab"><span class="tab-ico"></span>Transport</div>
  <div class="tab" style="height:60px"><span class="tab-ico"></span>Manufacturing of<br>Concrete Bricks &amp; Blocks</div>
  <div class="tab" style="height:58px"><span class="tab-ico"></span>Lightweight Concrete<br>Readymix</div>
</div>
<div class="abs panel">
  <h3>Construction</h3>
  <p>Lorem ipsum dolor sit amet, consectetuer adipiscing elit, sed diam nonummy nibh euismod tincidunt ut laoreet dolore magna aliquam erat volutpat. Ut wisi em ad minim veniam, quis nostrud tatullamcorper suscipit lobortis nisl ut aliquip e commodo consequat. Duis autem vel eumiure dolor in hendrerin vulputate velit esse molestie consequat, vel illum dolore.</p>
  <span class="btn">Read More</span>
  <div class="panel-photo" role="img" aria-label="Engineers in hard hats looking up at a glass building under construction"></div>
</div>

<!-- intro 1 -->
<div class="abs center h2" style="top:1794px">LOREM ISPIUM IS THE <b>DUMMY TEXT</b></div>
<div class="abs rule" style="top:1844px"></div>
<div class="abs copy" style="top:1862px">Lorem ipsum dolor sit amet, consectetuer adipiscing elit, sed diam nonummy nibh euismod tincidunt ut laoreet dolore magna aliquam erat volutpat. Ut wisi enim ad minim veniam, quis nostrud exerci tation ullamcorper suscipit lobortis nisl ut aliquip ex ea commodo consequat.</div>
<div class="abs btn-wrap" style="top:1932px"><span class="btn">Contact Us Today</span></div>

<!-- why choose -->
<div class="abs why" role="img" aria-label="Businessman in a suit with a city skyline, tinted deep blue"></div>
<div class="abs center h2" style="top:2070px;color:var(--blue-light)">WHY CHOOSE US</div>
<svg class="abs" style="left:0;top:2030px" width="1200" height="464" viewBox="0 0 1200 464">
  <path d="M370 377 A 230 230 0 0 1 830 377" fill="none" stroke="#9ccbee" stroke-width="2"/>
</svg>
<div class="abs arc"></div>
<div class="abs dot" style="left:471px;top:2373px"></div>
<div class="abs dot" style="left:539px;top:2326px"></div>
<div class="abs dot" style="left:649px;top:2326px"></div>
<div class="abs dot" style="left:717px;top:2373px"></div>
<div class="abs center arc-brand">VORLANE</div>

<div class="abs feat-ico" style="left:501px;top:2209px"><svg width="34" height="34" viewBox="0 0 16 18"><path d="M3 1l4 4-2 3c1 2 3 4 5 5l3-2 3 4-2 2C8 17 0 9 1 3z" fill="#0d3f78"/></svg></div>
<div class="abs feat-ico" style="left:630px;top:2198px"><svg width="34" height="34" viewBox="0 0 34 34"><circle cx="17" cy="11" r="7" fill="#0d3f78"/><path d="M4 32c0-8 6-12 13-12s13 4 13 12z" fill="#0d3f78"/></svg></div>
<div class="abs feat-ico" style="left:386px;top:2267px"><svg width="34" height="34" viewBox="0 0 34 34"><circle cx="17" cy="17" r="11" fill="none" stroke="#0d3f78" stroke-width="6" stroke-dasharray="5 3"/><circle cx="17" cy="17" r="4" fill="#0d3f78"/></svg></div>
<div class="abs feat-ico" style="left:745px;top:2265px"><svg width="34" height="34" viewBox="0 0 34 34"><rect x="4" y="6" width="26" height="24" rx="2" fill="none" stroke="#0d3f78" stroke-width="3"/><rect x="4" y="6" width="26" height="6" fill="#0d3f78"/><path d="M10 18h4M17 18h4M10 24h4M17 24h4" stroke="#0d3f78" stroke-width="3"/></svg></div>
<div class="abs feat-ico" style="left:331px;top:2368px"><svg width="34" height="34" viewBox="0 0 34 34"><circle cx="17" cy="14" r="8" fill="#0d3f78"/><rect x="13" y="23" width="8" height="6" fill="#0d3f78"/></svg></div>
<div class="abs feat-ico" style="left:802px;top:2366px"><svg width="34" height="34" viewBox="0 0 34 34"><circle cx="11" cy="11" r="5" fill="#0d3f78"/><circle cx="23" cy="11" r="5" fill="#0d3f78"/><path d="M2 30c0-7 4-11 9-11s9 4 9 11zM14 30c0-7 4-11 9-11s9 4 9 11z" fill="#0d3f78"/></svg></div>

<div class="abs feat" style="left:280px;top:2160px;width:200px"><h4>Unbiased Recommendations</h4>Lorem ipsum dolor sit mork<br>[+] ..adipiscing sed diam</div>
<div class="abs feat r" style="left:200px;top:2250px;width:170px"><h4>Unparalleled<br>Service</h4>Lorem ipsum dolor sit mork<br>[+] ..adipiscing sed diam</div>
<div class="abs feat r" style="left:130px;top:2386px;width:180px"><h4>Superior Advice</h4>Lorem ipsum dolor sit mork<br>[+] ..adipiscing sed diam</div>
<div class="abs feat" style="left:720px;top:2160px;width:200px"><h4>Expert Guidance</h4>Lorem ipsum dolor sit mork<br>adipiscing sed diam...[+]</div>
<div class="abs feat" style="left:839px;top:2258px;width:180px"><h4>Considerable Time<br>For You</h4>Lorem ipsum dolor sit mork<br>adipiscing sed diam...[+]</div>
<div class="abs feat" style="left:897px;top:2370px;width:200px"><h4>Deep Legal Industry<br>Relationships</h4>Lorem ipsum dolor sit mork<br>adipiscing sed diam...[+]</div>

<!-- intro 2 -->
<div class="abs center h2" style="top:2558px">LOREM ISPIUM IS THE <b>DUMMY TEXT</b></div>
<div class="abs rule" style="top:2608px"></div>
<div class="abs copy" style="top:2626px">Lorem ipsum dolor sit amet, consectetuer adipiscing elit, sed diam nonummy nibh euismod tincidunt ut laoreet dolore magna aliquam erat volutpat. Ut wisi enim ad minim veniam, quis nostrud exerci tation ullamcorper suscipit lobortis nisl ut aliquip ex ea commodo consequat.</div>
<div class="abs btn-wrap" style="top:2697px"><span class="btn">Contact Us Today</span></div>

<!-- contact -->
<div class="abs contact" role="img" aria-label="Dusky city skyline with a communications tower, dark tinted"></div>
<div class="abs center h2" style="top:2910px;color:var(--blue-light)">CONTACT US</div>
<div class="abs center c-line" style="top:2997px"><svg width="14" height="18" viewBox="0 0 14 18"><path d="M7 0a7 7 0 0 1 7 7c0 5-7 11-7 11S0 12 0 7a7 7 0 0 1 7-7z" fill="#3aa4f0"/><circle cx="7" cy="7" r="2.5" fill="#1d2a3b"/></svg>Street Name, City Name State Zipcode</div>
<div class="abs center c-line" style="top:3027px;font-size:14px"><svg width="24" height="16" viewBox="0 0 22 15"><rect x="1" y="1" width="20" height="13" fill="none" stroke="#3aa4f0" stroke-width="2"/><path d="M1 1l10 8 10-8" fill="none" stroke="#3aa4f0" stroke-width="2"/></svg>info@vorlane.co.za&nbsp;&nbsp;<svg width="20" height="22" viewBox="0 0 16 18"><path d="M3 1l4 4-2 3c1 2 3 4 5 5l3-2 3 4-2 2C8 17 0 9 1 3z" fill="#3aa4f0"/></svg>+27 (0) 21 555 0148</div>
<div class="abs center c-line" style="top:3073px;font-size:16px">Please Fill In The Following Fields &amp; We Will Be In Touch With You</div>
<div class="abs field" style="left:241px;top:3108px;width:232px;height:47px">Name</div>
<div class="abs field" style="left:483px;top:3108px;width:233px;height:47px">Phone</div>
<div class="abs field" style="left:726px;top:3108px;width:233px;height:47px">Email Address</div>
<div class="abs field" style="left:241px;top:3166px;width:718px;height:117px">Message</div>
<div class="abs send">Send Your Message</div>
<svg class="abs" style="left:0;top:3343px" width="1200" height="60" viewBox="0 0 1200 60"><polygon points="0,0 110,60 0,60" fill="#1b86d4"/><polygon points="1200,10 1080,60 1200,60" fill="#1b86d4"/></svg>
<div class="abs footer">Copyright© 2019 VORLANE BUILDING FORWARD. All Rights Reserved.</div>

</body>
</html>
```